3 signs to go on a trailer

due to logo change we need to update our trailer design signage the trailer has 3 panels 2 panels @ 650mmx1200 1@500mmx1200, i have attached a sample i was working on please feel free to change anything you feel needs change. im trying to achive a simple and soft design. i also uploaded our new logo in AI file, please feel free to contact me for further information. also a sketch of how the trailer looks like

```html
<!DOCTYPE html>
<html lang="en">
<head>
<meta charset="utf-8">
<title>Brightway trailer signage</title>
<link rel="stylesheet" href="https://fonts.googleapis.com/css2?family=Montserrat:wght@300;400;600;700&family=Arimo:wght@400&display=swap">
<style>
  :root {
    --bg-inner: #ffffff;
    --bg-outer: #ebebeb;
    --panel-edge: #9a9a9a;
    --text-grey: #3a3a3a;
    --orange: #f0822f;
    --orange-1: #ee8a3a;
    --orange-2: #f7ad4c;
    --orange-3: #f9d05a;
    --green-dark: #2c7a4b;
    --green: #45b35a;
    --green-light: #8cc97e;
    --wordmark: #58595b;
    --purple: #4a3f85;
    --purple-1: #5a4f9a;
    --purple-2: #7c72b6;
    --purple-3: #a39bcb;
    --white: #ffffff;
  }
  * { margin: 0; padding: 0; box-sizing: border-box; }
  html, body { width: 1200px; height: 900px; overflow: hidden; }
  body {
    position: relative;
    background: radial-gradient(ellipse at center, var(--bg-inner) 30%, var(--bg-outer) 100%);
    font-family: "Montserrat", sans-serif;
  }
  .panel {
    position: absolute;
    top: 172px;
    height: 555px;
    background: var(--white);
    border: 1px solid var(--panel-edge);
    overflow: hidden;
  }
  .panel--services { left: 89px; width: 300px; }
  .panel--brand { left: 484px; width: 232px; }
  .panel--blasting { left: 811px; width: 300px; }

  .heading {
    position: absolute;
    left: 22px;
    font-weight: 600;
    font-size: 21px;
    line-height: 20px;
    letter-spacing: -0.2px;
  }
  .services-heading { top: 72px; color: var(--orange); }
  .blasting-heading { top: 54px; color: var(--purple); }
  .blasting-heading .code { font-size: 10px; font-weight: 400; margin-left: 2px; }
  .list {
    position: absolute;
    left: 22px;
    list-style: none;
    font-weight: 300;
    font-size: 18px;
    line-height: 24px;
    color: var(--text-grey);
  }
  .services-list { top: 96px; }
  .blasting-list { top: 96px; }

  .colour-field {
    position: absolute;
    left: 0; right: 0; bottom: 0;
  }
  .colour-field--orange {
    top: 290px;
    background: linear-gradient(120deg, var(--orange-1) 0%, var(--orange-2) 55%, var(--orange-3) 100%);
  }
  .colour-field--purple {
    top: 290px;
    background: linear-gradient(120deg, var(--purple) 0%, var(--purple-2) 55%, var(--purple-3) 100%);
  }
  .colour-field--green {
    top: 440px;
    background: linear-gradient(110deg, var(--green) 0%, var(--green-light) 60%);
  }

  .contact {
    position: absolute;
    left: 0; right: 0;
    text-align: center;
  }
  .phone { font-weight: 700; font-size: 25px; letter-spacing: 0.5px; }
  .web { font-family: "Arimo", sans-serif; font-size: 18px; }
  .contact--light { top: 492px; color: var(--white); }
  .contact--light .web { margin-top: -4px; }

  .brand-mark {
    position: absolute;
    top: 82px; left: 50%;
    width: 90px; height: 90px;
    margin-left: -45px;
    border-radius: 50%;
    background: var(--green);
  }
  .brand-name {
    position: absolute;
    top: 244px; left: 0; right: 0;
    text-align: center;
    font-weight: 700;
    font-size: 27px;
    letter-spacing: 0.5px;
    color: var(--wordmark);
  }
  .contact--brand { top: 306px; color: var(--green-dark); }
  .contact--brand .web { font-size: 17px; margin-top: 0; }
</style>
</head>
<body>
  <section class="panel panel--services">
    <h2 class="heading services-heading">INTEGRATED SERVICES</h2>
    <ul class="list services-list">
      <li>CLEANING</li>
      <li>SECURITY</li>
      <li>MAINTENANCE</li>
    </ul>
    <div class="colour-field colour-field--orange" role="img" aria-label="Large decorative graphic in warm orange and yellow tones"></div>
    <div class="contact contact--light">
      <p class="phone">1300 555 014</p>
      <p class="web">www.brightway.com.au</p>
    </div>
  </section>

  <section class="panel panel--brand">
    <div class="brand-mark"></div>
    <h1 class="brand-name">BRIGHTWAY</h1>
    <div class="contact contact--brand">
      <p class="phone">1300 555 014</p>
      <p class="web">www.brightway.com.au</p>
    </div>
    <div class="colour-field colour-field--green" role="img" aria-label="Decorative band in soft green tones"></div>
  </section>

  <section class="panel panel--blasting">
    <h2 class="heading blasting-heading">WATER<br>BLASTING DIVISION<span class="code">TN003</span></h2>
    <ul class="list blasting-list">
      <li>5800PSI PRESSURE</li>
      <li>150°HOT WATER</li>
      <li>NO CHEMICALS</li>
      <li>100% ECO FRIENDLY</li>
    </ul>
    <div class="colour-field colour-field--purple" role="img" aria-label="Large decorative graphic in purple and lavender tones"></div>
    <div class="contact contact--light">
      <p class="phone">1300 555 014</p>
      <p class="web">www.brightway.com.au</p>
    </div>
  </section>
</body>
</html>
```